A Maverick Business Card for a Maverick Company!

We're a maverick, 'rule breaker' market research company that needs a maverick business card design to suit who we are!

All logos, colours and text are detailed in the attached briefing document.

Note Please ignore the 'Look & Feel' wizard results and refer ONLY to the attached brief.

```html
<!DOCTYPE html>
<html lang="en">
<head>
<meta charset="utf-8">
<title>Keystone Uprising – Pull Card</title>
<link rel="stylesheet" href="https://fonts.googleapis.com/css2?family=Open+Sans:wght@300;400;600&display=swap">
<style>
  :root{
    --red:#e0141b;
    --red-deep:#b30c12;
    --red-soft:#f4c9cb;
    --ink:#4a4a4a;
    --label:#d9d9d9;
    --card:#ffffff;
    --card-shade:#f1f1f1;
  }
  *{margin:0;padding:0;box-sizing:border-box}
  html,body{width:1200px;height:873px;overflow:hidden;background:#fff}
  body{position:relative;font-family:"Open Sans",Arial,sans-serif}

  .state-label{position:absolute;font-weight:300;font-size:36px;color:var(--label);letter-spacing:1px}
  .state-label--closed{left:11px;top:66px}
  .state-label--open{left:38px;top:722px}

  .card-closed{
    position:absolute;left:183px;top:66px;width:830px;height:476px;
    background:linear-gradient(118deg,var(--card-shade) 0%,var(--card-shade) 40%,var(--card) 40.2%,var(--card) 100%);
    border:1px solid #e4e4e4;
    box-shadow:0 4px 8px rgba(0,0,0,.35);
  }

  .brand{position:absolute;display:flex;align-items:center;color:var(--ink);font-weight:600;white-space:nowrap;line-height:1}
  .brand__dot{border-radius:50%;background:var(--ink)}
  .card-closed .brand{right:40px;top:74px;gap:16px;font-size:46px}
  .card-closed .brand__dot{width:40px;height:40px}

  .pull-zone{position:absolute;left:0;top:197px;width:830px;height:174px}
  .pull-text{position:absolute;left:636px;top:62px;font-size:36px;font-weight:600;color:var(--red)}
  .pull-tab{position:absolute;right:0;top:188px;filter:drop-shadow(-2px 2px 3px rgba(0,0,0,.3))}

  .card-open{
    position:absolute;left:178px;top:606px;width:294px;height:254px;
    box-shadow:0 3px 6px rgba(0,0,0,.35);
    clip-path:polygon(0 0,95% 0,100% 4%,100% 100%,0 100%);
    background:linear-gradient(180deg,#fff 0%,#fbe3e4 31%,var(--red) 31.5%,var(--red) 80%,#ee6d72 93%,var(--red-soft) 100%);
  }
  .card-open .brand{left:40px;top:22px;gap:8px;font-size:21px}
  .card-open .brand__dot{width:14px;height:14px}
  .contact-name{position:absolute;left:34px;top:140px;color:#fff;font-size:19px}
  .contact-role{position:absolute;left:42px;top:168px;color:#fff;font-size:9px}
  .divider{position:absolute;left:167px;top:90px;width:5px;height:120px;background:#fff}
  .contact-line{position:absolute;left:182px;color:#fff;font-size:15px;white-space:nowrap}
  .contact-line--phone{top:94px}
  .contact-line--fax{top:115px}
  .contact-line--mail{top:186px}
</style>
</head>
<body>
  <div class="state-label state-label--closed">Closed</div>

  <section class="card-closed">
    <div class="brand">
      <div class="brand__dot"></div>
      <div class="brand__name">Keystone Uprising</div>
    </div>

    <div class="pull-zone">
      <svg width="830" height="174" viewBox="0 0 830 174">
        <rect x="2" y="2" width="826" height="170" rx="40" fill="none" stroke="#e0141b" stroke-width="3" stroke-dasharray="8 6"/>
        <line x1="498" y1="87" x2="610" y2="87" stroke="#e0141b" stroke-width="5"/>
        <polygon points="488,87 520,70 520,104" fill="#e0141b"/>
      </svg>
      <div class="pull-text">Pull Me!</div>
    </div>

    <svg class="pull-tab" width="46" height="200" viewBox="0 0 46 200">
      <defs>
        <linearGradient id="tabFill" x1="0" y1="0" x2="1" y2="0">
          <stop offset="0" stop-color="#b30c12"/>
          <stop offset="1" stop-color="#ff2a30"/>
        </linearGradient>
      </defs>
      <path d="M46 0 L46 200 C36 176 8 160 8 100 C8 56 28 28 46 0 Z" fill="url(#tabFill)"/>
    </svg>
  </section>

  <div class="state-label state-label--open">Open</div>

  <section class="card-open">
    <div class="brand">
      <div class="brand__dot"></div>
      <div class="brand__name">Keystone Uprising</div>
    </div>
    <div class="contact-name">Mark Ellery</div>
    <div class="contact-role">Marketing Manager</div>
    <div class="divider"></div>
    <div class="contact-line contact-line--phone">Ph: 481920</div>
    <div class="contact-line contact-line--fax">Fax: 481920</div>
    <div class="contact-line contact-line--mail">mark@keyst</div>
  </section>
</body>
</html>
```